A graphic design for advertising on Tinsora

We are going to boost our new business with advertising on TS. Our startup business works based on a mobile app in which customers can get the different services including Massage therapy, Hair cut & makeup, house cleaning, oil change, and electronic device repair at their home /door.

The idea is a design showing a busy person getting a massage by a professional massage therapist while at the same time she is getting a hair cut by a hairstylist while a housekeeper is cleaning her place; along with a short explanatory text on the design in a way that doesn't make it look messy.
A bright and shiny background that delivers a feeling of relaxation and cleanness would work great. You can find the initial idea attached, however, any brilliant idea is more than welcome.

Target Market(s)

Every single people

Industry/Entity Type

App

Requirements
Must have
• The app is a platform connecting the customers to the service providers. The services are Tutoring, Massage therapy, hair styling, cleaning and automotive service jobs.
Nice to have
• Please dont limit yourself to the idea given in project description

```html
<!DOCTYPE html>
<html lang="en">
<head>
<meta charset="utf-8">
<title>lorem lorem – Services at your door step</title>
<link href="https://fonts.googleapis.com/css2?family=Montserrat:wght@400;500;600;700;800&display=swap" rel="stylesheet">
<style>
  :root {
    --bg-deep: #184e66;
    --bg-mid: #21647f;
    --bg-light: #2a7391;
    --yellow: #f9d94a;
    --red: #ee2657;
    --white: #ffffff;
    --phone-body: #0d2a2c;
    --screen: #bebebe;
    --footer-text: #7cbad4;
    --ring: #ffffff;
  }
  * { margin: 0; padding: 0; box-sizing: border-box; }
  html, body { width: 1200px; height: 1200px; overflow: hidden; }
  body { font-family: "Montserrat", sans-serif; }
  .poster {
    position: relative; width: 1200px; height: 1200px; overflow: hidden;
    background: radial-gradient(ellipse at 50% 40%, var(--bg-light) 0%, var(--bg-mid) 45%, var(--bg-deep) 100%);
  }
  .artwork { position: absolute; inset: 0; }
  .brand {
    position: absolute; left: 54px; top: 54px; display: flex; align-items: center; gap: 22px;
  }
  .brand-dot { width: 62px; height: 62px; border-radius: 50%; background: var(--red); }
  .brand-name { font-weight: 600; font-size: 35px; color: var(--white); letter-spacing: -0.5px; }
  .headline { position: absolute; left: 0; width: 1200px; text-align: center; }
  .headline-lead {
    top: 152px; font-weight: 800; font-size: 64px; color: var(--yellow); letter-spacing: 3px;
  }
  .headline-services {
    top: 231px; font-weight: 500; font-size: 20px; line-height: 26px; color: var(--white); letter-spacing: 4.6px;
  }
  .headline-tag {
    top: 282px; font-weight: 800; font-size: 70px; color: var(--white); letter-spacing: -2.5px;
  }
  .headline-tag .accent { color: var(--red); }
  .ribbon {
    position: absolute; top: 52px; right: -88px; width: 340px; height: 50px;
    background: var(--red); transform: rotate(45deg);
    color: var(--white); font-weight: 500; font-size: 21px; text-align: center; line-height: 50px;
  }
  .app-screen-brand {
    position: absolute; left: 445px; top: 700px; width: 300px;
    display: flex; align-items: center; justify-content: center; gap: 12px;
  }
  .app-screen-brand .brand-dot { width: 48px; height: 48px; }
  .app-screen-brand .brand-name { font-size: 29px; color: var(--red); }
  .contact-bar {
    position: absolute; left: 0; top: 1130px; width: 1200px; height: 70px;
    border-top: 1px solid rgba(124, 186, 212, 0.35);
  }
  .contact-item {
    position: absolute; top: 28px; font-size: 17px; font-weight: 400; color: var(--footer-text);
  }
  .contact-web { left: 149px; }
  .contact-mail { left: 509px; }
  .contact-phone { left: 976px; }
</style>
</head>
<body>
<main class="poster">
  <svg class="artwork" width="1200" height="1200" viewBox="0 0 1200 1200" xmlns="http://www.w3.org/2000/svg">
    <defs>
      <linearGradient id="tone-massage" x1="0" y1="0" x2="1" y2="1"><stop offset="0" stop-color="#e9c2a2"/><stop offset="1" stop-color="#b97a58"/></linearGradient>
      <linearGradient id="tone-haircut" x1="0" y1="0" x2="1" y2="1"><stop offset="0" stop-color="#3a3230"/><stop offset="1" stop-color="#9a7a68"/></linearGradient>
      <linearGradient id="tone-makeup" x1="0" y1="0" x2="1" y2="1"><stop offset="0" stop-color="#d7a98c"/><stop offset="1" stop-color="#8a5a44"/></linearGradient>
      <linearGradient id="tone-cleaning" x1="0" y1="0" x2="1" y2="1"><stop offset="0" stop-color="#e3e6e6"/><stop offset="1" stop-color="#a9b2b3"/></linearGradient>
      <linearGradient id="tone-oil" x1="0" y1="0" x2="1" y2="1"><stop offset="0" stop-color="#2e3c3e"/><stop offset="1" stop-color="#6c7a7a"/></linearGradient>
      <linearGradient id="tone-repair" x1="0" y1="0" x2="1" y2="1"><stop offset="0" stop-color="#5d4d3e"/><stop offset="1" stop-color="#b59a7c"/></linearGradient>
      <path id="arc-massage" d="M 210 582 A 99 99 0 0 1 408 582"/>
      <path id="arc-haircut" d="M 217 795 A 92 92 0 0 1 401 795"/>
      <path id="arc-makeup" d="M 217 1008 A 92 92 0 0 1 401 1008"/>
      <path id="arc-cleaning" d="M 788 585 A 99 99 0 0 1 986 585"/>
      <path id="arc-oil" d="M 795 805 A 92 92 0 0 1 979 805"/>
      <path id="arc-repair" d="M 795 1018 A 92 92 0 0 1 979 1018"/>
    </defs>

    <g class="phone">
      <ellipse cx="596" cy="1108" rx="170" ry="8" fill="#0d2f3e" opacity="0.4"/>
      <rect x="417" y="522" width="8" height="50" rx="3" fill="var(--phone-body)"/>
      <rect x="417" y="586" width="8" height="74" rx="3" fill="var(--phone-body)"/>
      <rect x="766" y="565" width="8" height="40" rx="3" fill="var(--phone-body)"/>
      <rect x="423" y="408" width="345" height="684" rx="52" fill="var(--phone-body)"/>
      <rect x="432" y="417" width="327" height="666" rx="44" fill="none" stroke="#ffffff" stroke-width="3"/>
      <rect x="566" y="441" width="58" height="5" rx="2.5" fill="#3a5657"/>
      <circle cx="656" cy="443" r="3.5" fill="#2a8ed0"/>
      <rect class="app-screen" x="445" y="474" width="300" height="527" fill="var(--screen)"/>
      <line x1="479" y1="984" x2="694" y2="984" stroke="#d8d8d8" stroke-width="2"/>
      <line x1="479" y1="984" x2="630" y2="984" stroke="#ffffff" stroke-width="2"/>
    </g>

    <g class="service-badges" fill="none" stroke="var(--ring)" stroke-width="4" stroke-dasharray="16 8">
      <circle cx="309" cy="582" r="80"/>
      <circle cx="309" cy="795" r="80"/>
      <circle cx="309" cy="1008" r="80"/>
      <circle cx="887" cy="585" r="80"/>
      <circle cx="887" cy="805" r="80"/>
      <circle cx="887" cy="1018" r="80"/>
    </g>
    <circle cx="309" cy="582" r="72" fill="url(#tone-massage)" role="img" aria-label="Photo of a woman receiving a back massage"/>
    <circle cx="309" cy="795" r="72" fill="url(#tone-haircut)" role="img" aria-label="Photo of a barber cutting a man's hair"/>
    <circle cx="309" cy="1008" r="72" fill="url(#tone-makeup)" role="img" aria-label="Photo of makeup being applied to a woman's eyes"/>
    <circle cx="887" cy="585" r="72" fill="url(#tone-cleaning)" role="img" aria-label="Photo of a gloved hand cleaning a window"/>
    <circle cx="887" cy="805" r="72" fill="url(#tone-oil)" role="img" aria-label="Photo of a mechanic doing an oil change"/>
    <circle cx="887" cy="1018" r="72" fill="url(#tone-repair)" role="img" aria-label="Photo of a technician repairing an electronic device"/>

    <g class="service-labels" font-family="Montserrat, sans-serif" font-weight="500" font-size="21" fill="#ffffff" text-anchor="middle">
      <text><textPath href="#arc-massage" startOffset="50%">MASSAGE THERAPY</textPath></text>
      <text><textPath href="#arc-haircut" startOffset="50%">HAIR CUT</textPath></text>
      <text><textPath href="#arc-makeup" startOffset="50%">MAKEUP</textPath></text>
      <text><textPath href="#arc-cleaning" startOffset="50%">HOUSE CLEANING</textPath></text>
      <text><textPath href="#arc-oil" startOffset="50%">OIL CHANGE</textPath></text>
      <text><textPath href="#arc-repair" startOffset="50%">DEVICE REPAIR</textPath></text>
    </g>

    <g class="contact-icons" fill="none" stroke="var(--footer-text)" stroke-width="2.5">
      <circle cx="111" cy="1165" r="19"/>
      <ellipse cx="111" cy="1165" rx="8" ry="19"/>
      <line x1="92" y1="1165" x2="130" y2="1165"/>
      <line x1="95" y1="1155" x2="127" y2="1155"/>
      <line x1="95" y1="1175" x2="127" y2="1175"/>
      <rect x="454" y="1154" width="38" height="24" rx="1"/>
      <polyline points="454,1154 473,1168 492,1154"/>
      <line x1="454" y1="1178" x2="468" y2="1165"/>
      <line x1="492" y1="1178" x2="478" y2="1165"/>
      <rect x="934" y="1144" width="28" height="46" rx="4"/>
      <line x1="934" y1="1180" x2="962" y2="1180"/>
      <circle cx="948" cy="1185" r="1.5" fill="var(--footer-text)"/>
    </g>
  </svg>

  <div class="brand">
    <span class="brand-dot"></span>
    <span class="brand-name">lorem lorem</span>
  </div>

  <div class="ribbon">SAVE YOUR TIME</div>

  <h1 class="headline headline-lead">WE PROVIDE</h1>
  <p class="headline headline-services">MASSAGE THERAPY, HAIR CUT &amp; MAKEUP, HOUSE CLEANING<br>OIL CHANGE, AND ELECTRONIC DEVICE REPAIR</p>
  <h2 class="headline headline-tag">AT YOUR <span class="accent">DOOR</span> STEP</h2>

  <div class="app-screen-brand">
    <span class="brand-dot"></span>
    <span class="brand-name">lorem lorem</span>
  </div>

  <footer class="contact-bar">
    <span class="contact-item contact-web">WWW.YOURWEBSITE.COM</span>
    <span class="contact-item contact-mail">YOURADDRESS@MAILNEST.COM</span>
    <span class="contact-item contact-phone">+01 8000 56 78</span>
  </footer>
</main>
</body>
</html>
```